I need a business card.

I need a simple, minimalist, business card. I think the coolest business card I have ever seen is Marty Vexler's from Brimstone Heist... it is just a little creepy for the real world.
I am a photographer and I need a card that I can give to brides or potential portrait customers that is simple and classy.
My name is Gil Anstrade. My website is www.gilanstrade-example.com
Please design my card.
I think it could be as simple as my name, phone # and website... where the rest of my contact could be found... or maybe my email and no website... I am open to ideas. I imagined the card on thick card stock with a black background...

```html
<!DOCTYPE html>
<html lang="en">
<head>
<meta charset="utf-8">
<title>Gil Anstrade — Business Card</title>
<link rel="stylesheet" href="https://fonts.googleapis.com/css2?family=Cormorant+Garamond:wght@600&family=Lora:wght@400&display=swap">
<style>
  :root {
    --stage: #2b2b2b;
    --card-top: #5a5a5a;
    --card-bottom: #1c1c1c;
    --photo-light: #d4d4d4;
    --photo-mid: #a8a8a8;
    --photo-dark: #6e6e6e;
    --ink-light: #f4f4f4;
    --ink-dark: #2a2a2a;
    --contact-light: #e6e6e6;
  }
  html, body {
    margin: 0;
    width: 1200px;
    height: 903px;
    overflow: hidden;
    background: var(--stage);
  }
  .stage {
    position: relative;
    width: 1200px;
    height: 903px;
  }
  .card {
    position: absolute;
    top: 296px;
    width: 526px;
    height: 310px;
    overflow: hidden;
    box-shadow: 0 6px 14px rgba(0,0,0,0.45);
  }
  .card--front {
    left: 50px;
    background: linear-gradient(180deg, var(--card-top) 0%, #333 55%, var(--card-bottom) 100%);
  }
  .card--back {
    left: 622px;
  }
  .card__photo {
    position: absolute;
    inset: 0;
    background:
      linear-gradient(180deg, var(--photo-light) 0%, #c2c2c2 45%, #8e8e8e 52%, var(--photo-mid) 60%, var(--photo-dark) 100%);
  }
  .card__contact {
    position: absolute;
    top: 22px;
    right: 40px;
    margin: 0;
    text-align: right;
    font-family: "Lora", Georgia, serif;
    font-size: 11.5px;
    line-height: 1.45;
    color: var(--contact-light);
  }
  .card--back .card__contact {
    color: var(--ink-dark);
  }
  .card__name {
    position: absolute;
    margin: 0;
    font-family: "Cormorant Garamond", "Times New Roman", serif;
    font-weight: 600;
    font-size: 84px;
    line-height: 0.78;
    letter-spacing: -1px;
    color: var(--ink-light);
    text-transform: uppercase;
  }
  .card--front .card__name {
    left: 34px;
    top: 110px;
  }
  .card--back .card__name {
    right: 18px;
    top: 110px;
    text-align: right;
  }
  .card__name span { display: block; }
</style>
</head>
<body>
<main class="stage">
  <section class="card card--front">
    <p class="card__contact">555.017.2248<br>gil@gilanstrade-example.com<br>www.gilanstrade-example.com</p>
    <h1 class="card__name"><span>Gil</span><span>Anstrade</span></h1>
  </section>
  <section class="card card--back">
    <div class="card__photo" role="img" aria-label="Black and white photograph of a couple embracing on a beach at the shoreline"></div>
    <p class="card__contact">555.017.2248<br>gil@gilanstrade-example.com<br>www.gilanstrade-example.com</p>
    <h2 class="card__name"><span>Gil</span><span>Anstrade</span></h2>
  </section>
</main>
</body>
</html>
```